Need new Spot UV Business Card design

We are looking for a new business card design incorporating Spot UV in black & white options / versions. See examples files and Mireno Castel Design logo.
You can see our website at www.mirenocastel-example.ca. We want something classy but yet modern. We are open to black or black and/or white on white with the spot uv. We are open to portrait or landscape. Size should be standard 3.5" x 2". The front of the card should focus on the logo and name "Mireno Castel" only. Fonts used should be "Open sans" or "PT Sans".

Target Market(s)

Mid to high end

Industry/Entity Type

Business

Contact Information for Business Card

Tobin Ferrash
555.304.8172
tobin@mirenocastel-example.ca
www.mirenocastel-example.ca
4917 Alderwick Blvd. W Suite 308
Mississauga, ON K7R 2B9

Requirements
Must have
• Name & Logo

```html
<!DOCTYPE html>
<html lang="en">
<head>
<meta charset="utf-8">
<title>Mireno Castel – Spot UV Business Card</title>
<link href="https://fonts.googleapis.com/css2?family=Open+Sans:wght@300;400;600;700&display=swap" rel="stylesheet">
<style>
  :root {
    --backdrop: #161616;
    --card: #2b2b2b;
    --card-back: #1f1f1f;
    --ink-light: #8c8c8c;
    --ink-mid: #7a7a7a;
    --gloss: #b9b9b9;
    --band: #2e2e2e;
    --rule: #3a3a3a;
  }
  * { box-sizing: border-box; margin: 0; padding: 0; }
  html, body {
    width: 1200px; height: 974px; overflow: hidden;
    background: radial-gradient(ellipse at 70% 35%, #2a2a2a 0%, var(--backdrop) 70%);
    font-family: "Open Sans", sans-serif;
  }
  .stage {
    position: relative; width: 1200px; height: 974px;
  }
  .card {
    position: absolute; width: 520px; height: 297px;
    border-radius: 3px;
    box-shadow: 0 18px 40px rgba(0,0,0,.6);
    overflow: hidden;
  }
  /* Front: logo + contact */
  .card--front {
    left: 50px; top: 410px; background: var(--card);
    display: flex;
  }
  .front__brand {
    width: 56%; display: flex; align-items: center; justify-content: center; gap: 14px;
  }
  .brand-square {
    width: 52px; height: 52px; border: 3px solid var(--ink-mid); flex: none;
  }
  .brand-name {
    color: var(--ink-mid); font-weight: 400; font-size: 30px; line-height: 1.0;
    letter-spacing: .5px; text-transform: uppercase;
  }
  .front__contact {
    width: 44%; border-left: 1px solid var(--rule);
    padding: 44px 0 0 24px; color: var(--ink-light);
  }
  .person__first { font-weight: 300; font-size: 16px; letter-spacing: 1px; text-transform: uppercase; }
  .person__last { font-weight: 700; font-size: 16px; letter-spacing: 1px; text-transform: uppercase; margin-bottom: 12px; }
  .contact-line { display: flex; align-items: center; gap: 7px; font-size: 11px; line-height: 19px; }
  .contact-line svg { width: 11px; height: 11px; flex: none; fill: none; stroke: var(--ink-light); stroke-width: 1.4; }
  .address { font-size: 11px; line-height: 17px; margin-top: 10px; }

  /* Back: spot UV field with name band */
  .card--back {
    left: 630px; top: 230px; background: var(--card-back);
  }
  .back__field {
    position: absolute; inset: 0;
    background: linear-gradient(160deg, #5a5a5a 0%, #333 40%, #1c1c1c 100%);
  }
  .back__band {
    position: absolute; left: 50%; top: 50%; transform: translate(-50%, -50%);
    display: flex; align-items: center; gap: 12px;
    background: var(--band); padding: 12px 22px;
    box-shadow: 0 0 0 1px #3b3b3b;
  }
  .back__band .brand-square { width: 28px; height: 28px; border-width: 2px; border-color: var(--gloss); }
  .back__band .brand-name { color: var(--gloss); font-size: 26px; font-weight: 600; }
</style>
</head>
<body>
<main class="stage">
  <section class="card card--back">
    <div class="back__field" role="img" aria-label="Spot UV gloss pattern of repeating diamond motifs across the card"></div>
    <div class="back__band">
      <span class="brand-square"></span>
      <span class="brand-name">Mireno Castel</span>
    </div>
  </section>

  <section class="card card--front">
    <div class="front__brand">
      <span class="brand-square"></span>
      <span class="brand-name">Mireno<br>Castel</span>
    </div>
    <div class="front__contact">
      <p class="person__first">Tobin</p>
      <p class="person__last">Ferrash</p>
      <p class="contact-line">
        <svg viewBox="0 0 12 12"><path d="M2.5 1.5l2 2-1 1.5c.8 1.5 2 2.7 3.5 3.5l1.5-1 2 2-1.3 1.5C5.5 10.5 1.5 6.5 1 2.8z"/></svg>
        555.304.8172
      </p>
      <p class="contact-line">
        <svg viewBox="0 0 12 12"><rect x="1" y="2.5" width="10" height="7"/><path d="M1 2.5l5 4 5-4"/></svg>
        tobin@mirenocastel-example.ca
      </p>
      <p class="contact-line">
        <svg viewBox="0 0 12 12"><circle cx="6" cy="6" r="5"/><ellipse cx="6" cy="6" rx="2.2" ry="5"/><path d="M1 6h10"/></svg>
        www.mirenocastel-example.ca
      </p>
      <p class="address">4917 Alderwick Blvd W #308<br>Mississauga, ON K7R 2B9</p>
    </div>
  </section>
</main>
</body>
</html>
```